Tarrow Building Ventures needs a Business card design and logo

We Need a business card design and logo for a Building & Construction business based in Melbourne. We work in both the Domestic & Commercial sector. We specialize in all aspects of building including extensions, Renovations, and alterations. Construction Management, Project Management, And labour hire
Updates

Industry/Entity Type

Business

```html
<!DOCTYPE html>
<html lang="en">
<head>
<meta charset="utf-8">
<title>Tarrow Building Ventures – Business Card</title>
<link rel="stylesheet" href="https://fonts.googleapis.com/css2?family=Michroma&family=Open+Sans:wght@400;600&family=Cormorant+SC:wght@600&display=swap">
<style>
  :root {
    --page-bg: #eef0f3;
    --card-white: #ffffff;
    --navy: #1f2f86;
    --brand-blue: #2b3f9c;
    --royal: #3a55b5;
    --sky-light: #d9f1fb;
    --sky-mid: #8fcfee;
    --sky-deep: #2f7fc4;
    --ink: #444a55;
    --tag-grey: #5c6270;
  }
  * { box-sizing: border-box; margin: 0; padding: 0; }
  html, body { width: 1200px; height: 784px; overflow: hidden; }
  body {
    background: var(--page-bg);
    display: flex;
    align-items: center;
    justify-content: center;
    gap: 40px;
  }
  .card {
    position: relative;
    width: 540px;
    height: 309px;
    border-radius: 4px;
    overflow: hidden;
    box-shadow: 0 6px 18px rgba(30, 40, 70, 0.18);
  }

  /* Back of card */
  .card-back {
    background: var(--sky-light);
  }
  .card-back .backdrop {
    position: absolute;
    inset: 0;
    width: 100%;
    height: 100%;
  }
  .services {
    position: absolute;
    left: 34px;
    top: 52px;
    list-style: none;
    font-family: "Michroma", sans-serif;
    font-size: 12px;
    letter-spacing: 2.5px;
    color: var(--navy);
  }
  .services li { height: 40px; }
  .services li:nth-child(2) { padding-left: 14px; }
  .services li:nth-child(3) { padding-left: 26px; }
  .services li:nth-child(4) { padding-left: 38px; }
  .services li:nth-child(5) { padding-left: 44px; }
  .back-brand {
    position: absolute;
    right: 26px;
    top: 150px;
    display: flex;
    align-items: center;
    gap: 8px;
    font-family: "Open Sans", sans-serif;
    font-weight: 600;
    font-size: 13px;
    color: var(--card-white);
  }
  .brand-square {
    width: 12px;
    height: 12px;
    background: var(--card-white);
  }

  /* Front of card */
  .card-front { background: var(--card-white); }
  .front-brand {
    position: absolute;
    left: 34px;
    top: 48px;
  }
  .brand-row {
    display: flex;
    align-items: center;
    gap: 10px;
  }
  .brand-row .brand-square {
    width: 22px;
    height: 22px;
    background: var(--brand-blue);
  }
  .brand-name {
    font-family: "Open Sans", sans-serif;
    font-weight: 600;
    font-size: 22px;
    color: var(--brand-blue);
    letter-spacing: 0.3px;
  }
  .tagline {
    margin-top: 6px;
    margin-left: 32px;
    font-family: "Open Sans", sans-serif;
    font-size: 10px;
    letter-spacing: 3.6px;
    color: var(--tag-grey);
    text-transform: uppercase;
  }
  .contact {
    position: absolute;
    left: 40px;
    top: 180px;
    font-family: "Open Sans", sans-serif;
    color: var(--ink);
  }
  .contact-name {
    font-size: 18px;
    font-weight: 600;
    color: var(--brand-blue);
    margin-bottom: 18px;
  }
  .contact-line {
    display: flex;
    align-items: center;
    gap: 6px;
    font-size: 13.5px;
    line-height: 20px;
  }
  .contact-line svg { width: 13px; height: 13px; flex: none; }
</style>
</head>
<body>

  <section class="card card-back" aria-label="Card back">
    <svg class="backdrop" viewBox="0 0 540 309" preserveAspectRatio="none" role="img" aria-label="Soft blue wireframe grid background">
      <defs>
        <linearGradient id="backGradient" x1="0" y1="0" x2="1" y2="0.4">
          <stop offset="0" stop-color="#e3f5fc"/>
          <stop offset="0.45" stop-color="#9fd7f1"/>
          <stop offset="1" stop-color="#2a78c2"/>
        </linearGradient>
      </defs>
      <rect width="540" height="309" fill="url(#backGradient)"/>
    </svg>
    <ul class="services">
      <li>- EXTENTIONS</li>
      <li>- RENOVATIONS</li>
      <li>- ALTERATIONS</li>
      <li>-DECKS</li>
      <li>-PARGOLAS</li>
    </ul>
    <div class="back-brand">
      <span class="brand-square"></span>
      <span>Tarrow Building Ventures</span>
    </div>
  </section>

  <section class="card card-front" aria-label="Card front">
    <div class="front-brand">
      <div class="brand-row">
        <span class="brand-square"></span>
        <span class="brand-name">Tarrow Building Ventures</span>
      </div>
      <p class="tagline">Domestic &amp; Commercial Builders</p>
    </div>

    <div class="contact">
      <p class="contact-name">Sam Tarrow</p>
      <p class="contact-line">
        <svg viewBox="0 0 16 16" aria-hidden="true"><rect x="4" y="1" width="8" height="14" rx="1.5" fill="#2b3f9c"/><rect x="5.5" y="3" width="5" height="8" fill="#fff"/></svg>
        0400 517 236
      </p>
      <p class="contact-line">
        <svg viewBox="0 0 16 16" aria-hidden="true"><path d="M3 1.5 L6 1.5 L7 5 L5.2 6.4 C6 8.3 7.7 10 9.6 10.8 L11 9 L14.5 10 L14.5 13 C14.5 14 13.6 14.6 12.6 14.5 C6.8 13.9 2.1 9.2 1.5 3.4 C1.4 2.4 2 1.5 3 1.5 Z" fill="#2b3f9c"/></svg>
        (03) 9015 47720
      </p>
      <p class="contact-line">
        <svg viewBox="0 0 16 16" aria-hidden="true"><rect x="1" y="3.5" width="14" height="9.5" rx="1" fill="#2b3f9c"/><path d="M1.5 4 L8 9 L14.5 4" fill="none" stroke="#fff" stroke-width="1.3"/></svg>
        info@tarrowbuildingventures.com
      </p>
    </div>
  </section>

</body>
</html>
```